Velisto Events Business Card

We need a business cards that stands out to our clients. We are company who targets prestige clients to spend money with us on experiences, so our image needs to be prestige
Target Market(s)
Corporate
Contact Information for Business Card
There will be four different names on the business cards
Dana Morrowby
Director
O: 02 5147 3086
M: 0451 692 038
E: info@velistoevents.example.au
Facebook: @velistoevents
Instagram: velistoevents
www.velistoevents.example.au
Nathaniel Morrowby
Director
O: 02 5147 3086
M: 0467 215 904
Facebook: @velistoevents
Instagram: velistoevents
www.velistoevents.example.au
Teodor Vinkel
Director
O: 02 5147 3086
M: 0478 903 527
Facebook: @velistoevents
Instagram: velistoevents
www.velistoevents.example.au
Mabel Hartung
Director
O: 02 5147 3086
Facebook: @velistoevents
Instagram: velistoevents
www.velistoevents.example.au
Colors
Designer to choose colors to be used in the design.
Look and feel

```html
<!DOCTYPE html>
<html lang="en">
<head>
<meta charset="utf-8">
<title>Velisto Events Business Card</title>
<link rel="stylesheet" href="https://fonts.googleapis.com/css2?family=Open+Sans:wght@400;600;700&display=swap">
<style>
  :root {
    --stage: #e4e4e6;
    --violet-deep: #3a3173;
    --violet-light: #524a94;
    --gold: #c9a95c;
    --gold-faint: #efe3c2;
    --paper: #f7f7f7;
    --ink: #111111;
    --ink-soft: #2a2a2a;
    --ink-muted: #555555;
    --white: #ffffff;
  }
  * { box-sizing: border-box; margin: 0; padding: 0; }
  html, body {
    width: 1200px; height: 1000px; overflow: hidden;
    background: var(--stage);
    font-family: "Open Sans", Arial, sans-serif;
  }
  .stage { position: relative; width: 1200px; height: 1000px; }
  .card {
    position: absolute; left: 320px; width: 560px; height: 340px;
    border-radius: 3px; overflow: hidden;
    box-shadow: 0 10px 28px rgba(0,0,0,0.22);
  }
  .card--back {
    top: 110px;
    background: radial-gradient(circle at 60% 40%, var(--violet-light), var(--violet-deep) 75%);
  }
  .brand {
    position: absolute; left: 0; right: 0; top: 110px;
    display: flex; align-items: center; justify-content: center; gap: 14px;
  }
  .brand__dot {
    width: 18px; height: 18px; border-radius: 50%; background: var(--gold);
  }
  .brand__name {
    color: var(--gold); font-weight: 600; font-size: 30px;
    letter-spacing: 6px; text-transform: uppercase;
  }
  .website {
    position: absolute; left: 0; right: 0; bottom: 56px;
    display: flex; align-items: center; justify-content: center; gap: 8px;
    color: var(--white); font-size: 15px;
  }
  .card--front { top: 550px; background: var(--paper); }
  .emblem-faint {
    position: absolute; right: -70px; top: 20px;
    width: 280px; height: 280px; border-radius: 50%;
    background: var(--gold-faint);
    display: flex; align-items: center; justify-content: center;
  }
  .emblem-faint__name {
    color: var(--gold); font-weight: 600; font-size: 20px;
    letter-spacing: 3px; text-transform: uppercase; opacity: 0.7;
    margin-right: 60px;
  }
  .person { position: absolute; left: 50px; top: 96px; }
  .person__name { color: var(--ink); font-weight: 700; font-size: 28px; line-height: 1.2; }
  .person__role { color: var(--ink-soft); font-size: 20px; margin-top: 4px; }
  .contacts {
    position: absolute; left: 50px; bottom: 40px; list-style: none;
    color: var(--ink-muted); font-size: 15px; line-height: 24px;
  }
  .contacts li { display: flex; align-items: center; gap: 10px; }
  .contacts svg { width: 13px; height: 13px; flex: none; }
  .social-mark { width: 12px; height: 12px; background: var(--ink-soft); border-radius: 2px; flex: none; }
  .social-mark--round { border-radius: 50%; }
</style>
</head>
<body>
<main class="stage">
  <section class="card card--back" aria-label="Card back">
    <div class="brand">
      <span class="brand__dot"></span>
      <span class="brand__name">Velisto Events</span>
    </div>
    <p class="website">
      <svg width="13" height="13" viewBox="0 0 16 16" aria-hidden="true">
        <circle cx="8" cy="8" r="7" fill="none" stroke="#fff" stroke-width="1.4"/>
        <ellipse cx="8" cy="8" rx="3" ry="7" fill="none" stroke="#fff" stroke-width="1.2"/>
        <line x1="1" y1="8" x2="15" y2="8" stroke="#fff" stroke-width="1.2"/>
      </svg>
      www.velistoevents.example.au
    </p>
  </section>

  <section class="card card--front" aria-label="Card front">
    <div class="emblem-faint"><span class="emblem-faint__name">Velisto</span></div>
    <div class="person">
      <h1 class="person__name">Dana Morrowby</h1>
      <p class="person__role">Director</p>
    </div>
    <ul class="contacts">
      <li>
        <svg viewBox="0 0 16 16" aria-hidden="true"><rect width="16" height="16" rx="2" fill="#2a2a2a"/><path d="M5 4l2 2-1 1.5c.6 1.3 1.5 2.2 2.5 2.5L10 9l2 2-1.5 1.5C7 12 4 9 3.5 5.5z" fill="#fff"/></svg>
        0451 692 038
      </li>
      <li>
        <svg viewBox="0 0 16 16" aria-hidden="true"><rect x="1" y="3" width="14" height="10" rx="1" fill="#2a2a2a"/><path d="M1.5 4l6.5 5 6.5-5" fill="none" stroke="#fff" stroke-width="1.2"/></svg>
        info@velistoevents.example.au
      </li>
      <li><span class="social-mark"></span>@velistoevents</li>
      <li><span class="social-mark social-mark--round"></span>velistoevents</li>
    </ul>
  </section>
</main>
</body>
</html>
```